RV park billboard

We need a billboard for cedar bend RV park . I was thinking about having a big orange in the background. We will have free fiber optic internet and each camper will have its own personal hotspot and we want that on the sign... Also the phone number with the area code... But I don't have the exact number yet. Size of sign will be 12 x 40
Updates
Make sure sign has Cedar Bend RV park on it
Target Market(s)
Plant turnaround workers
Look and feel

```html
<!DOCTYPE html>
<html lang="en">
<head>
<meta charset="utf-8">
<title>Cedar Bend RV Park – Billboard</title>
<link href="https://fonts.googleapis.com/css2?family=Rozha+One&family=PT+Sans:ital,wght@0,400;1,700&family=Yanone+Kaffeesatz:wght@500&display=swap" rel="stylesheet">
<style>
  :root{
    --orange:#ee7d1a;
    --orange-deep:#e8661f;
    --ink:#111111;
    --white:#ffffff;
    --sky-top:#fff6b0;
    --sky-low:#fdf2a6;
    --grass:#6cb33a;
    --grass-dark:#3f9a2f;
    --rv-light:#fbfbfb;
    --rv-shade:#cfcfcf;
    --page:#ffffff;
  }
  *{margin:0;padding:0;box-sizing:border-box}
  html,body{width:1200px;height:1200px;overflow:hidden;background:var(--page)}
  .billboard{
    position:absolute;left:50px;top:435px;width:1100px;height:330px;overflow:hidden;
  }
  .billboard-shapes{position:absolute;inset:0;width:1100px;height:330px}
  .text-block{position:absolute;left:0;width:470px;text-align:center}
  .brand-name{
    top:58px;
    font-family:"Yanone Kaffeesatz",sans-serif;font-weight:500;font-size:64px;line-height:1;
    color:var(--orange);display:flex;justify-content:center;align-items:center;gap:12px;
  }
  .brand-dot{width:30px;height:30px;border-radius:50%;background:var(--orange);display:inline-block}
  .park-title{
    top:122px;
    font-family:"Rozha One",serif;font-size:78px;line-height:1;color:var(--ink);letter-spacing:1px;
  }
  .tagline{
    top:205px;
    font-family:"PT Sans",sans-serif;font-size:16px;line-height:1.1;color:var(--ink);
  }
  .tagline-highlight{
    top:222px;
    font-family:"PT Sans",sans-serif;font-style:italic;font-weight:700;font-size:22px;line-height:1.1;color:var(--orange);
  }
  .contact-icons{
    position:absolute;left:159px;top:254px;width:151px;display:flex;justify-content:space-between;
  }
  .contact-icons svg{width:34px;height:34px}
  .footer-address,.footer-phone{
    font-family:"PT Sans",sans-serif;color:var(--white);line-height:1;
  }
  .footer-address{top:303px;font-size:9px}
  .footer-phone{top:316px;font-size:11px}
</style>
</head>
<body>
<div class="billboard">
  <svg class="billboard-shapes" viewBox="0 0 1100 330">
    <defs>
      <linearGradient id="sceneSky" x1="0" y1="0" x2="0" y2="1">
        <stop offset="0" stop-color="var(--sky-top)"/>
        <stop offset="0.6" stop-color="var(--sky-low)"/>
        <stop offset="0.72" stop-color="var(--grass)"/>
        <stop offset="1" stop-color="var(--grass-dark)"/>
      </linearGradient>
      <linearGradient id="rvTone" x1="0" y1="0" x2="1" y2="1">
        <stop offset="0" stop-color="var(--rv-light)"/>
        <stop offset="1" stop-color="var(--rv-shade)"/>
      </linearGradient>
    </defs>
    <rect class="scene-area" x="430" y="0" width="670" height="330" fill="url(#sceneSky)" role="img" aria-label="Landscape with a yellow sun, pale mountains, birds, orange trees and green rolling fields"/>
    <rect class="rv-illustration" x="523" y="82" width="465" height="238" rx="18" fill="url(#rvTone)" role="img" aria-label="Illustration of a white and black class C motorhome driving forward on a green road"/>
    <path class="panel-edge" d="M0 0 H484 C535 80 545 200 478 330 H0 Z" fill="var(--orange-deep)"/>
    <path class="edge-line" d="M493 0 Q522 40 534 100" fill="none" stroke="var(--ink)" stroke-width="2.5"/>
    <path class="panel-white" d="M0 0 H468 C518 90 522 205 462 248 C350 300 150 304 0 262 Z" fill="var(--white)"/>
    <path class="corner-accent" d="M0 0 H60 C30 20 10 45 0 80 Z" fill="var(--orange)"/>
  </svg>

  <div class="text-block brand-name">Cedar Bend<span class="brand-dot"></span></div>
  <div class="text-block park-title">RV PARK</div>
  <div class="text-block tagline">Free Fiber Optic Internet And Each Camper Will Have Its</div>
  <div class="text-block tagline-highlight">Own Personal Hotspot</div>

  <div class="contact-icons">
    <svg viewBox="0 0 32 32" aria-label="Phone">
      <circle cx="16" cy="16" r="16" fill="var(--orange)"/>
      <path d="M11 8.5c1-.6 2-.2 2.5.7l1.2 2.5c.4.8.1 1.6-.6 2l-1 .7c.7 2 2.2 3.6 4.2 4.4l.7-1c.5-.7 1.3-.9 2-.5l2.5 1.3c.9.5 1.2 1.5.6 2.4-1 1.6-2.7 2.3-4.6 1.6-4.4-1.6-7.6-4.8-9-9.2-.6-1.9.1-3.9 1.5-4.9z" fill="var(--white)"/>
    </svg>
    <svg viewBox="0 0 32 32" aria-label="Location">
      <circle cx="16" cy="16" r="16" fill="var(--orange)"/>
      <path d="M16 6.5a6.5 6.5 0 0 0-6.5 6.5c0 4.8 6.5 12.5 6.5 12.5s6.5-7.7 6.5-12.5A6.5 6.5 0 0 0 16 6.5z" fill="var(--white)"/>
      <circle cx="16" cy="13" r="2.6" fill="var(--orange)"/>
    </svg>
    <svg viewBox="0 0 32 32" aria-label="Wi-Fi hotspot">
      <circle cx="16" cy="16" r="16" fill="var(--orange)"/>
      <g fill="none" stroke="var(--white)" stroke-width="2.4" stroke-linecap="round">
        <path d="M7.5 13.5a12 12 0 0 1 17 0"/>
        <path d="M10.5 16.8a7.8 7.8 0 0 1 11 0"/>
        <path d="M13.5 20a3.6 3.6 0 0 1 5 0"/>
      </g>
      <circle cx="16" cy="23" r="1.6" fill="var(--white)"/>
    </svg>
  </div>

  <div class="text-block footer-address">Cedar Bend Road, Sulphur, Louisiana (Exit 21; follow the blue signs to gate)</div>
  <div class="text-block footer-phone">+1(555)014-2738</div>
</div>
</body>
</html>
```